a promotional poster design to promote our upcoming event. We want the date to be promoted as "Save the Date" for Sunday 4th July 2021.

Requirements
Must have
• the following text;

Save the Date! (stand out)
Sunday 4th July 2021 (stand out)
KTRB Family Mixed Netball Carnival
Nice to have
• make the date stand out. We want people to lock in the date we're promoting.

```html
<!DOCTYPE html>
<html lang="en">
<head>
<meta charset="utf-8">
<title>Save the Date – KTRB Family Mixed Netball Carnival</title>
<link href="https://fonts.googleapis.com/css2?family=Kalam:wght@300&family=Merriweather:wght@400;900&family=Oswald:wght@600&display=swap" rel="stylesheet">
<style>
  :root {
    --cream: #fdf5c4;
    --cream-light: #fffbe6;
    --red: #e01e26;
    --ink: #111111;
    --yellow: #fcd116;
    --white: #ffffff;
    --tagline: #c9b98a;
  }
  * { margin: 0; padding: 0; box-sizing: border-box; }
  html, body { width: 886px; height: 1200px; overflow: hidden; }
  body {
    position: relative;
    background: radial-gradient(ellipse at 50% 55%, var(--cream-light) 0%, var(--cream) 70%);
    color: var(--ink);
  }
  .brand {
    position: absolute; left: 34px; top: 40px; width: 156px;
    display: flex; flex-direction: column; align-items: center;
  }
  .brand-mark { width: 60px; height: 60px; background: var(--red); margin-bottom: 34px; }
  .brand-name {
    font-family: "Oswald", sans-serif; font-weight: 600; font-size: 14px;
    line-height: 1.1; text-align: center; letter-spacing: 0.2px; text-transform: uppercase;
  }
  .brand-tagline {
    font-family: "Merriweather", serif; font-size: 7.5px;
    color: var(--tagline); margin-top: 2px;
  }
  .headline { position: absolute; left: 0; top: 150px; width: 886px; height: 270px; }
  .headline-save, .headline-date {
    position: absolute; font-family: "Kalam", cursive; font-weight: 300;
    line-height: 1; color: var(--ink);
  }
  .headline-save { left: 244px; top: 8px; font-size: 158px; }
  .headline-date { left: 398px; top: 150px; font-size: 148px; }
  .headline-the {
    position: absolute; left: 266px; top: 164px;
    font-family: "Merriweather", serif; font-weight: 400; font-size: 66px; color: var(--red);
  }
  .date-band {
    position: absolute; left: 91px; top: 440px; width: 700px; height: 83px;
    background: var(--red);
    box-shadow: 0 22px 18px -14px rgba(0,0,0,0.35);
    display: flex; align-items: center; justify-content: center;
    font-family: "Merriweather", serif; font-weight: 900; font-size: 56px;
    color: var(--white); letter-spacing: -0.5px; white-space: nowrap;
  }
  .campaign-lettering {
    position: absolute; left: 184px; top: 592px; width: 534px; height: 476px;
    border-radius: 60px;
    background: radial-gradient(ellipse at 50% 55%, var(--yellow) 0%, var(--red) 55%, var(--ink) 100%);
  }
  .event-details {
    position: absolute; left: 0; top: 1082px; width: 886px; text-align: center;
    font-family: "Merriweather", serif; font-size: 31px; line-height: 36px; color: var(--ink);
  }
  .footer-band {
    position: absolute; left: 0; bottom: 0; width: 886px; height: 24px; background: var(--red);
  }
  .footer-band svg { position: absolute; left: 768px; top: 0; }
</style>
</head>
<body>
  <header class="brand">
    <span class="brand-mark"></span>
    <span class="brand-name">Kinta Riverbank<br>Health Service</span>
    <span class="brand-tagline">Healthy Families Together</span>
  </header>

  <h1 class="headline">
    <span class="headline-save">Save</span>
    <span class="headline-the">The</span>
    <span class="headline-date">Date!</span>
  </h1>

  <div class="date-band">Sunday - 4th July, 2021</div>

  <div class="campaign-lettering" role="img" aria-label="Area for hand-lettered campaign slogan in red and yellow on a black outline"></div>

  <p class="event-details">KTRB Family Mixed Netball Carnival<br>Nice to haveipsum</p>

  <div class="footer-band">
    <svg width="24" height="24" viewBox="0 0 24 24"><line x1="4" y1="0" x2="12" y2="24" stroke="#fdf5c4" stroke-width="3"/></svg>
  </div>
</body>
</html>
```